Looking for an amazing business card for a thriving DJ business

We need a business card design for a DJ company based in South Florida. The DJ company specializes in weddings, parties, bar mitzvahs, corporate events, proms, and reunions. We are looking for a modern, simple business card design. The card should state DJ Marlow K.
Updates

The name on the card should be DJ Marlow K

Industry/Entity Type

Entertainment Industry

Contact Information for Business Card

DJ Marlow K
415.282.6047
bxdjmarlowk@quillmail.example
https://www.facebook-example.net/DjMarlowK/
https://www.photogram-example.net/djmarlow.k/
www.djmarlowk.example

Font styles to use
Serif
Sans Serif

Requirements
Must have
• My business card has to be awesome.
Should not have
• The card has to have personality.

```html
<!DOCTYPE html>
<html lang="en">
<head>
<meta charset="utf-8">
<title>DJ Marlow K — Business Card</title>
<link rel="stylesheet" href="https://fonts.googleapis.com/css2?family=Arimo:wght@400;700&display=swap">
<style>
  :root {
    --gold: #c79f56;
    --slate: #525b59;
    --white: #ffffff;
    --backdrop: #1c1c1c;
  }
  * { margin: 0; padding: 0; box-sizing: border-box; }
  html, body {
    width: 1093px; height: 1200px; overflow: hidden;
    background: var(--backdrop);
    font-family: "Arimo", Arial, sans-serif;
  }
  .card {
    position: absolute; left: 264px; width: 580px; height: 357px;
    background: var(--gold); overflow: hidden;
  }
  .card--front { top: 226px; }
  .card--back { top: 620px; }

  .front-arc { position: absolute; left: 0; top: 0; }

  .brand-mark {
    position: absolute; border-radius: 50%;
    background: var(--white);
    display: flex; align-items: center; justify-content: center;
    color: var(--slate); font-weight: 700; letter-spacing: 0.5px;
  }
  .card--front .brand-mark { left: 42px; top: 105px; width: 146px; height: 146px; font-size: 19px; }
  .card--back .brand-mark { left: 212px; top: 69px; width: 158px; height: 158px; font-size: 21px; }

  .contact { position: absolute; left: 278px; top: 90px; color: var(--white); }
  .contact__name { font-size: 23px; font-weight: 700; letter-spacing: 0.3px; margin-bottom: 19px; }
  .contact__list { list-style: none; }
  .contact__item { display: flex; align-items: center; gap: 6px; font-size: 16.5px; line-height: 21px; white-space: nowrap; }
  .contact__item--social { font-size: 15px; letter-spacing: -0.2px; }
  .contact__gap { height: 24px; }
  .contact__icon { width: 15px; height: 15px; flex: none; }

  .services {
    position: absolute; left: 0; top: 269px; width: 100%; height: 65px;
    background: var(--slate); color: var(--white);
    display: flex; flex-direction: column; align-items: center; justify-content: center;
    font-size: 15.5px; line-height: 18.5px; letter-spacing: 0.2px;
  }
  .services__dot { margin: 0 9px; font-size: 13px; }
</style>
</head>
<body>
  <section class="card card--front">
    <svg class="front-arc" width="580" height="357" viewBox="0 0 580 357" aria-hidden="true">
      <path d="M0 0 H157 A214 214 0 0 1 163 357 H0 Z" fill="var(--slate)"/>
    </svg>
    <div class="brand-mark">Nightwave</div>

    <div class="contact">
      <h1 class="contact__name">DJ MARLOW K</h1>
      <ul class="contact__list">
        <li class="contact__item">
          <svg class="contact__icon" viewBox="0 0 24 24" aria-hidden="true"><path fill="#fff" d="M6.6 10.8a15.1 15.1 0 0 0 6.6 6.6l2.2-2.2a1 1 0 0 1 1-.25 11.4 11.4 0 0 0 3.6.57 1 1 0 0 1 1 1V20a1 1 0 0 1-1 1A17 17 0 0 1 3 4a1 1 0 0 1 1-1h3.5a1 1 0 0 1 1 1c0 1.25.2 2.45.57 3.57a1 1 0 0 1-.25 1z"/></svg>
          415.282.6047
        </li>
        <li class="contact__item">
          <svg class="contact__icon" viewBox="0 0 24 24" aria-hidden="true"><rect x="2" y="5" width="20" height="14" fill="#fff"/><path d="M2 5 L12 13 L22 5" stroke="var(--gold)" stroke-width="1.6" fill="none"/></svg>
          bxdjmarlowk@quillmail.example
        </li>
        <li class="contact__item">
          <svg class="contact__icon" viewBox="0 0 24 24" aria-hidden="true"><g fill="none" stroke="#fff" stroke-width="1.8"><circle cx="12" cy="12" r="9.5"/><ellipse cx="12" cy="12" rx="4.2" ry="9.5"/><path d="M2.5 12h19M4 7h16M4 17h16"/></g></svg>
          www.djmarlowk.example
        </li>
        <li class="contact__gap" aria-hidden="true"></li>
        <li class="contact__item contact__item--social">
          <svg class="contact__icon" viewBox="0 0 24 24" aria-hidden="true"><circle cx="12" cy="12" r="9" fill="none" stroke="#fff" stroke-width="2"/></svg>
          www.socialhub-example.net/DjMarlowK/
        </li>
        <li class="contact__item contact__item--social">
          <svg class="contact__icon" viewBox="0 0 24 24" aria-hidden="true"><circle cx="12" cy="12" r="9" fill="none" stroke="#fff" stroke-width="2"/></svg>
          www.photogram-example.net/djmarlow.k/
        </li>
      </ul>
    </div>
  </section>

  <section class="card card--back">
    <div class="brand-mark">Nightwave</div>
    <div class="services">
      <p>WEDDINGS<span class="services__dot">●</span>PARTIES<span class="services__dot">●</span>BAR MITZVAHS</p>
      <p>CORPORATE EVENTS<span class="services__dot">●</span>PROMS &amp; REUNIONS</p>
    </div>
  </section>
</body>
</html>
```